Packaging for new retail dips "Quorlets"

* We require packaging for our new retail dip range.
* We have a small "Our Story" write up that we would like somewhere...
* We have approx. 7 different flavours - Hommous, Mediterranean Olive, Beetroot, Tzatziki etc. We would like one design where we can change the colour panel and the name of the dip.
* We are looking for a modern, clean, gourmet looking design - not the usual dip packaging you see on supermarket shelves.
* See my inspiration photo's.
* The Dieline attached is to scale.
Updates
Project Deadline Extended
Reason: Extension due to Dielines and Measurements not uploaded when we thought they were.
Target Market(s)
Will be going into retail supermarkets.
Industry/Entity Type
Retail
Font styles to use
Colors
Designer to choose colors to be used in the design.
Requirements
Must have
- * Please use our 'Quorlets' logo on the front and on the front side (if possible).
Nice to have
- * 'taste is everything' somewhere...
Should not have
- * No photo's of dips or photo's in general.

```html
<!DOCTYPE html>
<html lang="en">
<head>
<meta charset="utf-8">
<title>Quorlets dip range – packaging fronts</title>
<link rel="stylesheet" href="https://fonts.googleapis.com/css2?family=Great+Vibes&family=Italianno&family=Libre+Baskerville:wght@400;700&display=swap">
<style>
  :root {
    --page: #ffffff;
    --frame: #555555;
    --card-line: #3a3a3a;
    --ink: #333333;
    --logo-ink: #5a5a5a;
    --beetroot: #7b2840;
    --hummous: #dc9a1a;
    --tzatziki: #238b30;
    --olive: #948200;
    --white: #ffffff;
  }
  * { box-sizing: border-box; margin: 0; padding: 0; }
  html, body { width: 1200px; height: 1000px; overflow: hidden; background: var(--page); }
  .sheet {
    position: relative; width: 1200px; height: 1000px;
    border: 1px solid var(--frame); background: var(--page);
  }
  .pack {
    position: absolute; width: 416px; height: 416px;
    border: 1px solid var(--card-line); background: var(--white); overflow: hidden;
  }
  .pack--beetroot  { left: 132px; top: 61px;  --accent: var(--beetroot); }
  .pack--hummous   { left: 590px; top: 61px;  --accent: var(--hummous); }
  .pack--tzatziki  { left: 132px; top: 516px; --accent: var(--tzatziki); }
  .pack--olive     { left: 590px; top: 516px; --accent: var(--olive); }

  .brand {
    position: absolute; left: 22px; top: 52px;
    font-family: "Libre Baskerville", serif; font-size: 14px; letter-spacing: 2px;
    color: var(--logo-ink);
  }

  .story { position: absolute; left: 198px; top: -1px; width: 216px; height: 152px; }
  .story svg { position: absolute; inset: 0; }
  .story__title {
    position: absolute; left: 0; right: 0; top: 8px; text-align: center;
    font-family: "Libre Baskerville", serif; font-size: 15px; color: var(--white);
  }
  .story__text {
    position: absolute; left: 21px; right: 12px; top: 32px;
    font-family: "Libre Baskerville", serif; font-size: 8.3px; line-height: 18.5px;
    color: var(--white); white-space: nowrap;
  }

  .flavour {
    position: absolute; right: 26px; top: 168px; text-align: right;
    font-family: "Great Vibes", cursive; font-weight: 400; font-size: 46px; line-height: 46px;
    color: var(--accent);
  }
  .pack--olive .flavour { top: 160px; font-size: 44px; line-height: 46px; right: 28px; }

  .tagline {
    position: absolute; right: 26px; top: 268px;
    font-family: "Italianno", cursive; font-size: 30px; color: var(--ink);
  }
  .weight {
    position: absolute; right: 22px; top: 324px;
    font-family: "Libre Baskerville", serif; font-weight: 700; font-size: 15px; color: var(--ink);
  }
  .base-rule { position: absolute; left: 0; right: 0; top: 349px; height: 3px; background: var(--card-line); }
  .colour-panel { position: absolute; left: 0; right: 0; top: 352px; bottom: 0; background: var(--accent); }

  .product-image { position: absolute; border-radius: 6px; }
  .product-image--beetroot { left: 22px; top: 236px; width: 140px; height: 88px;
    background: radial-gradient(ellipse at 50% 60%, #8a2440 0%, #b05a6a 55%, #ffffff 100%); }
  .product-image--hummous { left: 24px; top: 244px; width: 142px; height: 78px;
    background: radial-gradient(ellipse at 55% 55%, #e8d6b0 0%, #e79a5c 50%, #ffffff 100%); }
  .product-image--tzatziki { left: 15px; top: 190px; width: 125px; height: 148px; border-radius: 0;
    background: linear-gradient(160deg, #f4f4f2 0%, #e4ebe2 55%, #cfd9cc 100%); }
  .product-image--olive { left: 18px; top: 242px; width: 142px; height: 92px;
    background: radial-gradient(ellipse at 55% 55%, #3e4a1c 0%, #8b9a4a 50%, #ffffff 100%); }
</style>
</head>
<body>
<main class="sheet">

  <section class="pack pack--beetroot">
    <div class="brand">QUORLETS</div>
    <div class="story">
      <svg viewBox="0 0 216 152" width="216" height="152" aria-hidden="true">
        <polygon points="0,0 216,0 216,152 108,128 0,152" fill="var(--beetroot)"/>
        <polyline points="5,0 5,144 108,121 211,144 211,0" fill="none" stroke="#fff" stroke-width="2"/>
      </svg>
      <p class="story__title">Our story...</p>
      <p class="story__text">Made in small batches from<br>fresh local produce, our dips<br>began at a family table and<br>still follow the same recipe<br>today.....</p>
    </div>
    <h2 class="flavour">Beetroot</h2>
    <div class="product-image product-image--beetroot" role="img" aria-label="Photo of fresh beetroot with leaves"></div>
    <p class="tagline">taste is everything</p>
    <p class="weight">200mg</p>
    <div class="base-rule"></div>
    <div class="colour-panel"></div>
  </section>

  <section class="pack pack--hummous">
    <div class="brand">QUORLETS</div>
    <div class="story">
      <svg viewBox="0 0 216 152" width="216" height="152" aria-hidden="true">
        <polygon points="0,0 216,0 216,152 108,128 0,152" fill="var(--hummous)"/>
        <polyline points="5,0 5,144 108,121 211,144 211,0" fill="none" stroke="#fff" stroke-width="2"/>
      </svg>
      <p class="story__title">Our story...</p>
      <p class="story__text">Made in small batches from<br>fresh local produce, our dips<br>began at a family table and<br>still follow the same recipe<br>today.....</p>
    </div>
    <h2 class="flavour">Hummous</h2>
    <div class="product-image product-image--hummous" role="img" aria-label="Photo of a bowl of hummous with vegetable sticks and flatbread"></div>
    <p class="tagline">taste is everything</p>
    <p class="weight">200mg</p>
    <div class="base-rule"></div>
    <div class="colour-panel"></div>
  </section>

  <section class="pack pack--tzatziki">
    <div class="brand">QUORLETS</div>
    <div class="story">
      <svg viewBox="0 0 216 152" width="216" height="152" aria-hidden="true">
        <polygon points="0,0 216,0 216,152 108,128 0,152" fill="var(--tzatziki)"/>
        <polyline points="5,0 5,144 108,121 211,144 211,0" fill="none" stroke="#fff" stroke-width="2"/>
      </svg>
      <p class="story__title">Our story...</p>
      <p class="story__text">Made in small batches from<br>fresh local produce, our dips<br>began at a family table and<br>still follow the same recipe<br>today.....</p>
    </div>
    <h2 class="flavour">Tzatziki</h2>
    <div class="product-image product-image--tzatziki" role="img" aria-label="Photo of a bowl of tzatziki with cucumber slices and herbs"></div>
    <p class="tagline">taste is everything</p>
    <p class="weight">200mg</p>
    <div class="base-rule"></div>
    <div class="colour-panel"></div>
  </section>

  <section class="pack pack--olive">
    <div class="brand">QUORLETS</div>
    <div class="story">
      <svg viewBox="0 0 216 152" width="216" height="152" aria-hidden="true">
        <polygon points="0,0 216,0 216,152 108,128 0,152" fill="var(--olive)"/>
        <polyline points="5,0 5,144 108,121 211,144 211,0" fill="none" stroke="#fff" stroke-width="2"/>
      </svg>
      <p class="story__title">Our story...</p>
      <p class="story__text">Made in small batches from<br>fresh local produce, our dips<br>began at a family table and<br>still follow the same recipe<br>today.....</p>
    </div>
    <h2 class="flavour">Mediterranean<br>Olive</h2>
    <div class="product-image product-image--olive" role="img" aria-label="Photo of green and black olives with an olive branch"></div>
    <p class="tagline">taste is everything</p>
    <p class="weight">200mg</p>
    <div class="base-rule"></div>
    <div class="colour-panel"></div>
  </section>

</main>
</body>
</html>
```